Plimsoo car advertisement

de website moet uit minimaal 3 pagina's bestaan. 1 pagina als een landingspagina. 1 pagina voor consumenten die hun auto willen laten beplakken met bedrijfsreclame en 1 pagina voor bedrijven / consumenten die hun bedrijfsreclame op een consumentenauto wilt plaatsen.

de website moet echt een happy website zijn. consumenten kunnen geld verdienen met reclame op hun auto te laten zetten en bedrijven kunnen voor een relatief goedkoop bedrag hun bedrijfsreclame op een auto laten zetten. die auto rijdt dan rond en veel mensen zien de reclame.

beide pagina's moeten dus een glimlach opleveren.

het doel van de startpagina is dat je door kunt gaan naar de consumenten en de bedrijfspagina.

gebruik leuke, vrolijke kleuren en vormen en zorg dat de mensen een glimlach krijgen als ze naar de website kijken.

doelgroep is consumenten die een auto rijden en geld willen verdienen met hun auto en de zakelijke ondernemer die voor een goedkoop bedrag zijn bedrijfsreclame met een full carwrap kan laten zien aan de buitenwereld.

doordat consumenten zich bij ons aanmelden hebben wij een database met auto's en weten we hoeveel deze auto's rijden en in welke regio's ze rijden en wat voor auto ze rijden. allemaal hele belangrijke informatie voor een ondernemer die reclame wilt maken op ene specifieke auto type en in een bepaalde regio.

-

website should consist of at least 3 pages. 1 landing page, 1 customer page and 1 business page. landing page let's the visitor choose wether he / she is a customer with a car and wants to allow his car to be fully carwrapped or he / she is a business owner who wants to place his advertisement on a car.

website should be a really happy joyfull website and bring a smile to the visitor. beause the customer can earn money (200 euro / month nett) by allowing advertisements on his car (full car wrap) and the business owner because for a low price he can advertise.

when customers that owns a car register themselves with our website we build a database with cars in specific locations. a business owner wants to advertise his product into a specific region. this is very valuable information.

agreement is 1 year for a customer to have advertisements on his car and for a business to advertise. after that year, the advertisements are safely removed from the car and new advertisement agreements can be made. a business can place advertisements (full carwrap) already for 795 euro's., Details for my new Web Design Project will be added soon. , de website moet uit minimaal 3 pagina's bestaan. 1 pagina als een landingspagina. 1 pagina voor consumenten die hun auto willen laten beplakken met bedrijfsreclame en 1 pagina voor bedrijven / consumenten die hun bedrijfsreclame op een consumentenauto wilt plaatsen.

Target Market(s)

customers who has a car
businesses who want to advertise their business / product on a car

Industry/Entity Type

Business

Requirements
Must have
• website should be playfull, colorfull and a joy to look at and work with. altough functoinality is very limited visitors need to be intrigued to proceed to contact plimsoo.
Nice to have
• nice graphics, moving images, a "living" website (not so static)

```html
<!DOCTYPE html>
<html lang="en">
<head>
<meta charset="utf-8">
<title>Plimsoo Car</title>
<link href="https://fonts.googleapis.com/css2?family=Questrial&display=swap" rel="stylesheet">
<style>
  :root{
    --orange:#ff9e00;
    --orange-deep:#f08a00;
    --orange-light:#ffb41e;
    --sky:#3aa6dc;
    --sky-deep:#0d5fa6;
    --sky-pale:#cfe9f7;
    --ink:#1b1b1b;
    --band:#1a1a1a;
    --white:#ffffff;
    --grey:#cfcfcf;
    --text:#333333;
    --link:#3aa4e0;
    --rule:#e3e3e3;
  }
  *{box-sizing:border-box;margin:0;padding:0}
  html,body{width:1200px;height:1000px;overflow:hidden;background:var(--white)}
  body{font-family:"Questrial",sans-serif;color:var(--text);position:relative}

  .hero{position:absolute;left:0;top:0;width:1200px;height:446px;
    background:
      radial-gradient(ellipse 420px 90px at 300px 210px,rgba(255,255,255,.85),rgba(255,255,255,0) 70%),
      radial-gradient(ellipse 500px 60px at 900px 150px,rgba(10,40,140,.7),rgba(10,40,140,0) 70%),
      linear-gradient(170deg,#9fd0ee 0%,var(--sky) 35%,var(--sky-deep) 60%,#5fb7e6 80%,#8fd0f0 100%);}
  .topbar{position:absolute;left:0;top:0;width:1200px;height:104px;background:rgba(255,255,255,.55)}
  .brand{position:absolute;left:12px;top:24px;font-size:40px;color:var(--white);letter-spacing:.5px;line-height:1}
  .brand .accent{color:var(--orange)}
  .slogan{position:absolute;left:11px;top:71px;font-size:20px;color:var(--ink)}
  .nav{position:absolute;top:0;left:615px;height:104px;display:flex}
  .nav a{display:block;height:104px;line-height:106px;font-size:18px;color:#3a3a3a;text-decoration:none;text-align:center}
  .nav a.current{background:rgba(255,255,255,.55);color:#111;width:139px}
  .nav .about{width:152px}.nav .services{width:145px}.nav .contacts{width:146px}
  .tab-fold{position:absolute;left:615px;top:62px}

  .choice{position:absolute;top:168px;width:260px;height:93px;border:3px solid var(--white);border-radius:8px;
    background:linear-gradient(var(--orange-light),var(--orange-deep));color:var(--ink);font-size:24px;line-height:29px;padding:18px 0 0 20px}
  .choice.customer{left:12px}.choice.owner{left:342px}
  .choice svg{position:absolute;right:12px;top:24px}

  .intro{position:absolute;left:14px;top:306px;width:500px;font-size:20px;line-height:24.5px;color:var(--white)}
  .intro .more{color:var(--ink)}
  .car{position:absolute;left:572px;top:176px;width:614px;height:270px;border-radius:120px 60px 30px 30px;
    background:linear-gradient(180deg,#1c1c2a 0%,#7a1a14 45%,#a0281e 70%,#2a2a2a 100%)}

  .band{position:absolute;left:0;top:446px;width:1200px;height:310px;background:var(--band)}
  .band h2{position:absolute;left:13px;top:84px;font-size:19px;font-weight:400;color:var(--orange)}
  .band p{position:absolute;left:13px;top:140px;width:330px;font-size:14px;line-height:17px;color:var(--grey)}
  .band p .more{color:var(--link)}
  .collage{position:absolute;left:360px;top:414px}

  .foot-brand{position:absolute;left:13px;top:830px;font-size:24px;color:var(--ink);line-height:1}
  .foot-brand .accent{color:var(--orange)}
  .foot-slogan{position:absolute;left:13px;top:856px;font-size:14px;color:var(--ink)}
  .copyright{position:absolute;left:12px;top:923px;font-size:12px;color:#444}
  .foot-col h3{font-size:19px;font-weight:400;color:#333;margin-bottom:15px}
  .foot-col.ticks{position:absolute;left:471px;top:828px;width:240px}
  .ticks li{list-style:none;height:40px;line-height:40px;border-bottom:1px solid var(--rule);font-size:12px;color:#333;padding-left:28px;position:relative}
  .ticks li svg{position:absolute;left:2px;top:14px}
  .foot-col.links{position:absolute;left:944px;top:828px}
  .links li{list-style:none;font-size:12px;line-height:23px;color:#333;padding-left:2px}
</style>
</head>
<body>
<header class="hero">
  <div class="topbar"></div>
  <div class="brand">PLIMSOO <span class="accent">CAR</span></div>
  <div class="slogan">Slogan Goes Here</div>
  <svg class="tab-fold" width="139" height="42" viewBox="0 0 139 42"><polygon points="0,42 14,0 139,42" fill="rgba(255,255,255,.45)"/></svg>
  <nav class="nav">
    <a class="current" href="#">HOME</a>
    <a class="about" href="#">ABOUT US</a>
    <a class="services" href="#">SERVICES</a>
    <a class="contacts" href="#">CONTACTS</a>
  </nav>

  <a class="choice customer">Plimsoo<br>Customer
    <svg width="48" height="48" viewBox="0 0 48 48"><circle cx="24" cy="24" r="22" fill="none" stroke="#fff" stroke-width="3"/><polygon points="18,12 34,24 18,36 23,24" fill="#fff"/></svg>
  </a>
  <a class="choice owner">Plimsoo<br>Business Owner
    <svg width="48" height="48" viewBox="0 0 48 48"><circle cx="24" cy="24" r="22" fill="none" stroke="#fff" stroke-width="3"/><polygon points="18,12 34,24 18,36 23,24" fill="#fff"/></svg>
  </a>

  <p class="intro">Lorem Ipsum is simply dummy text of the printing and typesetting industry. Lorem Ipsum has been the industry's.. <span class="more">+read more</span></p>
  <div class="car" role="img" aria-label="Illustration of a wrapped hatchback car with a space-themed advertising design"></div>
</header>

<section class="band">
  <h2>Lorem Ipsum is simply dummy</h2>
  <p>Lorem Ipsum is simply dummy text of the printing and typesetting industry. Lorem Ipsum has been the industry's&nbsp; typesetting industry. Lorem Ipsum has been the industry's.. <span class="more">+read more</span></p>
</section>
<svg class="collage" width="840" height="362" viewBox="0 0 840 362" role="img" aria-label="Photos of technicians applying advertising wrap film to cars">
  <defs>
    <linearGradient id="shotA" x1="0" y1="0" x2="1" y2="1"><stop offset="0" stop-color="#d8dde2"/><stop offset=".6" stop-color="#9aa4ad"/><stop offset="1" stop-color="#c23a2c"/></linearGradient>
    <linearGradient id="shotB" x1="0" y1="0" x2="1" y2="1"><stop offset="0" stop-color="#c9dff0"/><stop offset=".5" stop-color="#3f78c8"/><stop offset="1" stop-color="#2a2a2a"/></linearGradient>
    <linearGradient id="shotC" x1="0" y1="0" x2="1" y2="0"><stop offset="0" stop-color="#e8eef3"/><stop offset=".5" stop-color="#5a8fd6"/><stop offset="1" stop-color="#d7dce0"/></linearGradient>
  </defs>
  <polygon points="3,132 437,11 185,341" fill="url(#shotA)"/>
  <polygon points="288,166 655,4 828,300" fill="url(#shotB)"/>
  <polygon points="180,362 330,190 825,312 780,342" fill="url(#shotC)"/>
</svg>

<footer>
  <div class="foot-brand">PLIMSOO <span class="accent">CAR</span></div>
  <div class="foot-slogan">Slogan Goes Here</div>
  <div class="copyright">© All Right Reserved. Plimsoo Car</div>

  <div class="foot-col ticks">
    <h3>Lorem Ipsum is simply dummy</h3>
    <ul>
      <li><svg width="16" height="12" viewBox="0 0 16 12"><polyline points="1,6 6,11 15,1" fill="none" stroke="#aaa" stroke-width="2.5"/></svg>Lorem Ipsum is simply dummy</li>
      <li><svg width="16" height="12" viewBox="0 0 16 12"><polyline points="1,6 6,11 15,1" fill="none" stroke="#aaa" stroke-width="2.5"/></svg>Lorem Ipsum is simply dummy</li>
      <li><svg width="16" height="12" viewBox="0 0 16 12"><polyline points="1,6 6,11 15,1" fill="none" stroke="#aaa" stroke-width="2.5"/></svg>Lorem Ipsum is simply dummy</li>
    </ul>
  </div>

  <div class="foot-col links">
    <h3>Lorem Ipsum is simply dummy</h3>
    <ul>
      <li>Lorem Ipsum is simply dummy</li>
      <li>Lorem Ipsum is simply dummy</li>
      <li>Lorem Ipsum is simply dummy</li>
    </ul>
  </div>
</footer>
</body>
</html>
```